social interest sharing site needs a web site design

we need a web site design for a social web platform.
the site is one page(main page), that is split into 3 sections
each section is a different color(red,green and blue)
and a user can choose to share each of the sections.
any section/color will contain boxes , each box can contain different media types.

the media types:
* list of URLS
* list of articles including title + image + description
* list of videos
* thumbnails of images
* calender
* list of emails

the main content will look like corkboardly layout
multiple boxes each box can contain different type of content as described above

each color is a different tab
each tab will have layout like corkboardly
Updates

please read the last description update.
and i uploaded an image that can explain the requirements better

thanks
Oren
 

Industry/Entity Type

Media

```html
<!DOCTYPE html>
<html lang="en">
<head>
<meta charset="utf-8">
<title>Huebox — My Home Page</title>
<link rel="stylesheet" href="https://fonts.googleapis.com/css2?family=Ubuntu:wght@400;500;700&family=Open+Sans:wght@400;600;700&display=swap">
<style>
:root{
  --page:#e8e8e8;
  --topbar:#232426;
  --header:#2e3135;
  --tab-bg:#393b3e;
  --muted:#9a9c9f;
  --red:#ea4440;
  --green:#7ec443;
  --blue:#5ba6de;
  --card:#ffffff;
  --line:#e4e4e4;
  --text:#222;
  --body-text:#666;
  --icon:#7a7a7a;
  --link:#4a90d9;
}
*{box-sizing:border-box;margin:0;padding:0}
html,body{width:1200px;height:1000px;overflow:hidden}
body{position:relative;background:var(--page);font-family:"Open Sans",Arial,sans-serif;color:var(--text)}

.topbar{position:absolute;left:0;top:0;width:1200px;height:26px;background:var(--topbar)}
.quick-tabs{position:absolute;left:268px;top:4px;display:flex;gap:7px}
.quick-tab{height:17px;padding:0 8px;background:var(--tab-bg);color:#c9cacc;font-size:9px;line-height:17px;border-radius:1px}
.user-bar{position:absolute;left:652px;top:0;height:26px;display:flex;align-items:center;gap:0;font-size:9px;color:var(--muted)}
.user-bar .sep{width:1px;height:26px;background:#34363a;margin:0 8px}
.avatar{width:17px;height:17px;background:#3a3c40;display:flex;align-items:end;justify-content:center;margin-right:7px}
.user-bar b{color:#fff;font-weight:600}
.stat{display:flex;align-items:center;gap:4px;margin-left:10px}

.site-header{position:absolute;left:0;top:26px;width:1200px;height:57px;background:var(--header);border-bottom:1px solid #1c1d1f}
.brand{position:absolute;left:268px;top:11px;display:flex;align-items:center;gap:8px}
.brand-mark{width:30px;height:30px;background:var(--red)}
.brand-name{font-family:Ubuntu,sans-serif;font-weight:500;font-size:27px;color:#fff;letter-spacing:-.5px}
.main-nav{position:absolute;left:535px;top:14px;display:flex;align-items:center}
.nav-item{height:27px;line-height:27px;font-size:9.5px;font-weight:600;text-transform:uppercase;padding:0 11px;margin-right:3px}
.nav-item.home{background:var(--red);color:#fff}
.nav-item.videos{color:var(--green)}
.nav-item.apps{color:var(--blue)}
.social{position:absolute;top:16px;width:23px;height:23px;background:var(--red)}

.board{position:absolute;left:268px;top:98px;display:flex;gap:10px}
.column{width:159px;display:flex;flex-direction:column;gap:9px}
.card{background:var(--card);box-shadow:0 1px 2px rgba(0,0,0,.12)}
.media{width:100%;position:relative}
.card-body{padding:8px 9px 0}
.card-title{font-family:Ubuntu,sans-serif;font-size:11.5px;font-weight:500;line-height:15px;margin-bottom:6px;color:#222}
.card-text{font-size:7.3px;line-height:10.6px;color:var(--body-text)}
.card-foot{height:25px;border-top:1px solid var(--line);display:flex;align-items:center;padding:0 9px;gap:7px}
.share{width:10px;height:10px;background:var(--icon);border-radius:1px}
.comments{margin-left:auto;display:flex;align-items:center;gap:4px;font-size:8.5px;color:#888}
.link-list,.email-list{list-style:none;padding:9px 9px 0}
.link-list li{font-size:7.8px;line-height:15px;color:var(--link);text-decoration:underline}
.email-list li{font-size:7.8px;line-height:15.4px;color:#444}
.play{position:absolute;left:50%;top:50%;transform:translate(-50%,-50%)}

.calendar{padding-bottom:4px}
.cal-head{height:22px;background:var(--red);color:#fff;display:flex;align-items:center;justify-content:space-between;padding:0 12px;font-size:8.5px;font-weight:700}
.cal-grid{display:grid;grid-template-columns:repeat(7,1fr);text-align:center}
.cal-grid .dow{font-size:5.5px;color:#777;height:10px;line-height:10px;background:#f3f3f3;border-bottom:1px solid var(--line)}
.cal-grid .day{position:relative;font-size:7.5px;height:18px;line-height:18px;color:#333;border-right:1px solid #f0f0f0;border-bottom:1px solid #f0f0f0}
.cal-grid .day.other{color:#bbb}
.cal-grid .day.today{background:var(--red);color:#fff;font-weight:700}
.cal-grid .day.mark::before{content:"";position:absolute;left:1px;top:1px;border-top:5px solid #aaa;border-right:5px solid transparent}
.tooltip{position:absolute;left:114px;top:52px;width:38px;height:13px;background:#555;color:#fff;font-size:7px;font-weight:700;line-height:13px;text-align:center;border-radius:2px}

.site-footer{position:absolute;left:268px;top:967px;width:664px;height:33px;border-top:1px solid #d0d0d0;text-align:center;font-size:7.5px;color:#999;line-height:31px}
.to-top{position:absolute;right:0;top:-9px;width:36px;height:42px;background:#fff;border:1px solid #ddd;border-bottom:0;display:flex;align-items:center;justify-content:center}
</style>
</head>
<body>

<header class="topbar">
  <nav class="quick-tabs">
    <span class="quick-tab">Mayas favourites Videos</span>
    <span class="quick-tab">Talias pics + favourites links</span>
    <span class="quick-tab">Family weekly calendar and notes</span>
  </nav>
  <div class="user-bar">
    <span class="sep"></span>
    <span class="avatar"><svg width="12" height="13" viewBox="0 0 12 13"><circle cx="6" cy="4" r="3" fill="#707276"/><path d="M0 13c0-4 3-5 6-5s6 1 6 5z" fill="#707276"/></svg></span>
    <span>Welcome, <b>orensch</b></span>
    <span class="sep"></span>
    <span class="stat"><svg width="12" height="9" viewBox="0 0 12 9"><circle cx="4" cy="2.5" r="2" fill="#777"/><circle cx="8.5" cy="2.5" r="2" fill="#777"/><path d="M0 9c0-3 2-4 4-4s4 1 4 4zM6 9c0-3 1-4 2.5-4S12 6 12 9z" fill="#777"/></svg>142 Followers</span>
    <span class="stat"><svg width="10" height="10" viewBox="0 0 10 10"><path d="M0 4h2v6H0zM3 4l2-4c1 0 1.5.5 1.2 2L6 3.5h3.2c.6 0 .9.5.8 1l-1 4.5c-.1.6-.5 1-1 1H3z" fill="#777"/></svg>52 Likes</span>
    <span class="stat" style="margin-left:12px"><svg width="12" height="12" viewBox="0 0 12 12"><circle cx="6" cy="6" r="3.6" fill="none" stroke="#777" stroke-width="2.4" stroke-dasharray="2 1.2"/><circle cx="6" cy="6" r="1.3" fill="#777"/></svg></span>
  </div>
</header>

<header class="site-header">
  <div class="brand"><span class="brand-mark"></span><span class="brand-name">Huebox</span></div>
  <nav class="main-nav">
    <span class="nav-item home">My Home Page</span>
    <span class="nav-item videos">My Favourites Videos</span>
    <span class="nav-item apps">Personal Apps</span>
  </nav>
  <span class="social" style="left:877px" aria-label="Share on social network 1"></span>
  <span class="social" style="left:909px" aria-label="Share on social network 2"></span>
</header>

<main class="board">
  <!-- column 1 -->
  <div class="column">
    <article class="card">
      <div class="media" role="img" aria-label="Photo of a modern house interior with wooden staircase" style="height:167px;background:linear-gradient(160deg,#c9d2cf 0%,#6f6a5c 45%,#7a4a2a 80%,#4a2e1d 100%)"></div>
      <div class="card-body" style="height:78px"><h3 class="card-title">Awesome!</h3><p class="card-text">Stunning Estate on Sunset Strip HouseIdeas, a daily source for inspiration and fresh ideas on interior design and home decoration.</p></div>
      <footer class="card-foot"><i class="share"></i><i class="share"></i><span class="comments"><svg width="14" height="11" viewBox="0 0 14 11"><path d="M0 0h14v8H5l-3 3V8H0z" fill="#888"/></svg>20</span></footer>
    </article>
    <article class="card">
      <ul class="link-list" style="height:75px"><li>www.loremipsum.test</li><li>www.loremipsumdolor.test</li><li>www.anotherlinkhere.test</li><li>www.website.test</li></ul>
      <footer class="card-foot"><i class="share"></i><i class="share"></i><span class="comments"><svg width="14" height="11" viewBox="0 0 14 11"><path d="M0 0h14v8H5l-3 3V8H0z" fill="#888"/></svg>20</span></footer>
    </article>
    <article class="card">
      <div class="media" role="img" aria-label="Photo of a yellow labrador wearing a flower wreath" style="height:167px;background:linear-gradient(180deg,#5d6f3f 0%,#b59a6a 45%,#d8b98a 70%,#7d8a52 100%)"></div>
      <div class="card-body" style="height:78px"><h3 class="card-title">Sweet Yellow Lab</h3><p class="card-text">Stunning Estate on Sunset Strip HouseIdeas, a daily source for inspiration and fresh ideas on interior design and home decoration.</p></div>
      <footer class="card-foot"><i class="share"></i><i class="share"></i><span class="comments"><svg width="14" height="11" viewBox="0 0 14 11"><path d="M0 0h14v8H5l-3 3V8H0z" fill="#888"/></svg>20</span></footer>
    </article>
    <article class="card calendar" style="position:relative">
      <div class="cal-head"><span>◄</span><span>December 2012</span><span>►</span></div>
      <div class="cal-grid">
        <span class="dow">SUN</span><span class="dow">MON</span><span class="dow">TUE</span><span class="dow">WED</span><span class="dow">THU</span><span class="dow">FRI</span><span class="dow">SAT</span>
        <span class="day">1</span><span class="day">2</span><span class="day">3</span><span class="day">4</span><span class="day">5</span><span class="day">6</span><span class="day">7</span>
        <span class="day mark">8</span><span class="day">9</span><span class="day">10</span><span class="day">11</span><span class="day">12</span><span class="day">13</span><span class="day">14</span>
        <span class="day">15</span><span class="day">16</span><span class="day">17</span><span class="day">18</span><span class="day">19</span><span class="day">20</span><span class="day">21</span>
        <span class="day">22</span><span class="day">23</span><span class="day">24</span><span class="day">25</span><span class="day today">26</span><span class="day">27</span><span class="day">28</span>
        <span class="day">29</span><span class="day">30</span><span class="day mark">31</span><span class="day other">1</span><span class="day other">2</span><span class="day other">3</span><span class="day other">4</span>
      </div>
      <span class="tooltip">Event</span>
    </article>
  </div>

  <!-- column 2 -->
  <div class="column">
    <article class="card">
      <div class="media" role="img" aria-label="Photo of a snowy mountain above a harbour at sunset" style="height:131px;background:linear-gradient(180deg,#3d5f95 0%,#d98a5a 40%,#c7b3a8 62%,#2f4b7a 85%,#c25a3a 100%)"></div>
      <footer class="card-foot" style="height:27px"><i class="share"></i><i class="share"></i><span class="comments"><svg width="14" height="11" viewBox="0 0 14 11"><path d="M0 0h14v8H5l-3 3V8H0z" fill="#888"/></svg>20</span></footer>
    </article>
    <article class="card">
      <div class="media" role="img" aria-label="Video still of raspberry swirl cupcakes" style="height:167px;background:linear-gradient(160deg,#e9dccb 0%,#b8434a 45%,#c9a79a 70%,#7d1f2a 100%)">
        <svg class="play" width="50" height="50" viewBox="0 0 50 50"><circle cx="25" cy="25" r="23" fill="rgba(0,0,0,.12)" stroke="#fff" stroke-width="2.5"/><path d="M20 16l14 9-14 9z" fill="#fff"/></svg>
      </div>
      <div class="card-body" style="height:52px"><h3 class="card-title">Raspberry cupcakes recipe</h3><p class="card-text">Awesome video cupcake recipe!</p></div>
      <footer class="card-foot"><i class="share"></i><i class="share"></i><span class="comments"><svg width="14" height="11" viewBox="0 0 14 11"><path d="M0 0h14v8H5l-3 3V8H0z" fill="#888"/></svg>20</span></footer>
    </article>
    <article class="card">
      <div class="media" role="img" aria-label="Illustration of winter trees on a pale green background" style="height:167px;background:linear-gradient(160deg,#e3eee9 0%,#b9d2c6 50%,#8fb1a3 100%)"></div>
      <div class="card-body" style="height:30px"><h3 class="card-title">January</h3></div>
      <footer class="card-foot"><i class="share"></i><i class="share"></i><span class="comments"><svg width="14" height="11" viewBox="0 0 14 11"><path d="M0 0h14v8H5l-3 3V8H0z" fill="#888"/></svg>20</span></footer>
    </article>
    <article class="card">
      <ul class="email-list" style="height:106px"><li>emailaddress@email.com</li><li>email@email.com</li><li>anotheremail@email.com</li><li>email@email.com</li><li>anotheremail@email.com</li><li>email@email.com</li></ul>
      <footer class="card-foot"><i class="share"></i><i class="share"></i><span class="comments"><svg width="14" height="11" viewBox="0 0 14 11"><path d="M0 0h14v8H5l-3 3V8H0z" fill="#888"/></svg>20</span></footer>
    </article>
  </div>

  <!-- column 3 -->
  <div class="column">
    <article class="card">
      <div class="media" role="img" aria-label="Illustration of winter trees on a pale green background" style="height:167px;background:linear-gradient(160deg,#e3eee9 0%,#b9d2c6 50%,#8fb1a3 100%)"></div>
      <div class="card-body" style="height:30px"><h3 class="card-title">January</h3></div>
      <footer class="card-foot"><i class="share"></i><i class="share"></i><span class="comments"><svg width="14" height="11" viewBox="0 0 14 11"><path d="M0 0h14v8H5l-3 3V8H0z" fill="#888"/></svg>20</span></footer>
    </article>
    <article class="card">
      <ul class="email-list" style="height:106px"><li>emailaddress@email.com</li><li>email@email.com</li><li>anotheremail@email.com</li><li>email@email.com</li><li>anotheremail@email.com</li><li>email@email.com</li></ul>
      <footer class="card-foot"><i class="share"></i><i class="share"></i><span class="comments"><svg width="14" height="11" viewBox="0 0 14 11"><path d="M0 0h14v8H5l-3 3V8H0z" fill="#888"/></svg>20</span></footer>
    </article>
    <article class="card">
      <div class="media" role="img" aria-label="Photo of a modern house interior with wooden staircase" style="height:167px;background:linear-gradient(160deg,#c9d2cf 0%,#6f6a5c 45%,#7a4a2a 80%,#4a2e1d 100%)"></div>
      <div class="card-body" style="height:78px"><h3 class="card-title">Awesome!</h3><p class="card-text">Stunning Estate on Sunset Strip HouseIdeas, a daily source for inspiration and fresh ideas on interior design and home decoration.</p></div>
      <footer class="card-foot"><i class="share"></i><i class="share"></i><span class="comments"><svg width="14" height="11" viewBox="0 0 14 11"><path d="M0 0h14v8H5l-3 3V8H0z" fill="#888"/></svg>20</span></footer>
    </article>
    <article class="card">
      <div class="media" role="img" aria-label="Photo of a snowy mountain above a harbour at sunset" style="height:131px;background:linear-gradient(180deg,#3d5f95 0%,#d98a5a 40%,#c7b3a8 62%,#2f4b7a 85%,#c25a3a 100%)"></div>
      <footer class="card-foot" style="height:29px"><i class="share"></i><i class="share"></i><span class="comments"><svg width="14" height="11" viewBox="0 0 14 11"><path d="M0 0h14v8H5l-3 3V8H0z" fill="#888"/></svg>20</span></footer>
    </article>
  </div>

  <!-- column 4 -->
  <div class="column">
    <article class="card">
      <div class="media" role="img" aria-label="Photo of a yellow labrador wearing a flower wreath" style="height:167px;background:linear-gradient(180deg,#5d6f3f 0%,#b59a6a 45%,#d8b98a 70%,#7d8a52 100%)"></div>
      <div class="card-body" style="height:78px"><h3 class="card-title">Sweet Yellow Lab</h3><p class="card-text">Stunning Estate on Sunset Strip HouseIdeas, a daily source for inspiration and fresh ideas on interior design and home decoration.</p></div>
      <footer class="card-foot"><i class="share"></i><i class="share"></i><span class="comments"><svg width="14" height="11" viewBox="0 0 14 11"><path d="M0 0h14v8H5l-3 3V8H0z" fill="#888"/></svg>20</span></footer>
    </article>
    <article class="card calendar" style="position:relative">
      <div class="cal-head"><span>◄</span><span>December 2012</span><span>►</span></div>
      <div class="cal-grid">
        <span class="dow">SUN</span><span class="dow">MON</span><span class="dow">TUE</span><span class="dow">WED</span><span class="dow">THU</span><span class="dow">FRI</span><span class="dow">SAT</span>
        <span class="day">1</span><span class="day">2</span><span class="day">3</span><span class="day">4</span><span class="day">5</span><span class="day">6</span><span class="day">7</span>
        <span class="day mark">8</span><span class="day">9</span><span class="day">10</span><span class="day">11</span><span class="day">12</span><span class="day">13</span><span class="day">14</span>
        <span class="day">15</span><span class="day">16</span><span class="day">17</span><span class="day">18</span><span class="day">19</span><span class="day">20</span><span class="day">21</span>
        <span class="day">22</span><span class="day">23</span><span class="day">24</span><span class="day">25</span><span class="day today">26</span><span class="day">27</span><span class="day">28</span>
        <span class="day">29</span><span class="day">30</span><span class="day mark">31</span><span class="day other">1</span><span class="day other">2</span><span class="day other">3</span><span class="day other">4</span>
      </div>
      <span class="tooltip">Event</span>
    </article>
    <article class="card">
      <div class="media" role="img" aria-label="Video still of raspberry swirl cupcakes" style="height:167px;background:linear-gradient(160deg,#e9dccb 0%,#b8434a 45%,#c9a79a 70%,#7d1f2a 100%)">
        <svg class="play" width="50" height="50" viewBox="0 0 50 50"><circle cx="25" cy="25" r="23" fill="rgba(0,0,0,.12)" stroke="#fff" stroke-width="2.5"/><path d="M20 16l14 9-14 9z" fill="#fff"/></svg>
      </div>
      <div class="card-body" style="height:52px"><h3 class="card-title">Raspberry cupcakes recipe</h3><p class="card-text">Awesome video cupcake recipe!</p></div>
      <footer class="card-foot"><i class="share"></i><i class="share"></i><span class="comments"><svg width="14" height="11" viewBox="0 0 14 11"><path d="M0 0h14v8H5l-3 3V8H0z" fill="#888"/></svg>20</span></footer>
    </article>
    <article class="card">
      <ul class="link-list" style="height:75px"><li>www.loremipsum.test</li><li>www.loremipsumdolor.test</li><li>www.anotherlinkhere.test</li><li>www.website.test</li></ul>
      <footer class="card-foot"><i class="share"></i><i class="share"></i><span class="comments"><svg width="14" height="11" viewBox="0 0 14 11"><path d="M0 0h14v8H5l-3 3V8H0z" fill="#888"/></svg>20</span></footer>
    </article>
  </div>
</main>

<footer class="site-footer">
  Copyright@Huebox.All Rights Reserved
  <span class="to-top"><svg width="14" height="24" viewBox="0 0 14 24"><path d="M7 2v22M1 8l6-6 6 6" fill="none" stroke="#999" stroke-width="1.3"/></svg></span>
</footer>

</body>
</html>
```